Letterhead/Business Cards
w/new logo
Project: Letterhead/Business Cards
Letterhead/Business Cards - Packaging
Creative Brief
Professional
Wade Lindqvist
President
2718 W. Callory St. Louis, MO 48217
wadel@corvinsacks.com
corvinsacks.com

```html
<!DOCTYPE html>
<html lang="en">
<head>
<meta charset="utf-8">
<title>Corvin Sacks – Business Cards</title>
<link href="https://fonts.googleapis.com/css2?family=Open+Sans:ital,wght@0,400;0,600;0,700;1,600&display=swap" rel="stylesheet">
<style>
  :root {
    --page: #e9eaec;
    --card: #ffffff;
    --navy: #1f3f8f;
    --blue: #2d5fc4;
    --blue-light: #4f86e0;
    --red: #c8242f;
    --ink: #2a3550;
    --muted: #5b6478;
  }
  * { box-sizing: border-box; margin: 0; padding: 0; }
  html, body {
    width: 1200px; height: 939px; overflow: hidden;
    background: var(--page);
    font-family: "Open Sans", Arial, sans-serif;
  }
  .sheet {
    width: 1200px; height: 939px;
    display: flex; flex-direction: column; align-items: center; justify-content: center;
    gap: 44px;
  }
  .card {
    width: 700px; height: 400px;
    background: var(--card);
    position: relative; overflow: hidden;
    box-shadow: 0 6px 18px rgba(20, 30, 60, 0.12);
  }
  .brand {
    display: flex; align-items: center; gap: 10px;
    color: var(--navy); font-weight: 700; letter-spacing: 0.06em;
  }
  .brand-dot { border-radius: 50%; background: var(--red); flex: none; }
  .card-front { display: flex; align-items: center; justify-content: center; }
  .card-front .brand { font-size: 34px; }
  .card-front .brand-dot { width: 20px; height: 20px; }

  .card-back .swoosh { position: absolute; inset: 0; }
  .card-back .brand { position: absolute; left: 40px; top: 40px; font-size: 17px; gap: 7px; }
  .card-back .brand-dot { width: 11px; height: 11px; }
  .address {
    position: absolute; left: 40px; top: 88px;
    font-size: 12px; line-height: 1.5; color: var(--muted);
  }
  .person { position: absolute; right: 40px; top: 150px; text-align: right; }
  .person-name { font-size: 21px; font-weight: 600; font-style: italic; color: var(--navy); }
  .person-title { font-size: 15px; color: var(--blue); margin-top: 2px; }
  .contacts {
    position: absolute; right: 40px; top: 218px; list-style: none;
    font-size: 12px; line-height: 1.65; color: var(--ink); text-align: right;
  }
  .contacts li { display: flex; align-items: center; justify-content: flex-end; gap: 6px; }
  .contacts svg { width: 11px; height: 11px; fill: var(--navy); }
  .website {
    position: absolute; right: 120px; bottom: 26px;
    font-size: 15px; font-weight: 600; color: #ffffff; letter-spacing: 0.02em;
  }
</style>
</head>
<body>
<main class="sheet">
  <section class="card card-front" aria-label="Card front">
    <div class="brand"><span class="brand-dot"></span>CORVIN SACKS INC</div>
  </section>

  <section class="card card-back" aria-label="Card back">
    <svg class="swoosh" viewBox="0 0 700 400" preserveAspectRatio="none" aria-hidden="true">
      <defs>
        <linearGradient id="blueBand" x1="0" y1="0" x2="1" y2="0">
          <stop offset="0" stop-color="#1f3f8f"/>
          <stop offset="0.6" stop-color="#2d5fc4"/>
          <stop offset="1" stop-color="#1f3f8f"/>
        </linearGradient>
      </defs>
      <path d="M0 238 C 160 250, 300 280, 430 330 C 520 362, 620 380, 700 384 L700 390 C 610 386, 510 368, 420 338 C 290 292, 150 262, 0 252 Z" fill="var(--red)"/>
      <path d="M0 262 C 170 272, 300 302, 420 348 C 520 384, 610 400, 700 400 L0 400 Z" fill="#ffffff"/>
      <path d="M0 268 C 160 276, 300 306, 410 350 C 500 384, 600 398, 700 398 L700 400 L0 400 Z" fill="url(#blueBand)" opacity="0.15"/>
      <path d="M180 400 C 300 355, 430 330, 560 320 C 620 316, 670 316, 700 318 L700 400 Z" fill="url(#blueBand)"/>
      <path d="M180 400 C 300 360, 430 335, 560 326 C 620 322, 670 322, 700 324" fill="none" stroke="var(--blue-light)" stroke-width="3"/>
    </svg>

    <div class="brand"><span class="brand-dot"></span>CORVIN SACKS INC</div>
    <p class="address">2718 W. Callory<br>St. Louis, MO<br>48217</p>

    <div class="person">
      <p class="person-name">Wade Lindqvist</p>
      <p class="person-title">President</p>
    </div>

    <ul class="contacts">
      <li>314 555 0182
        <svg viewBox="0 0 24 24"><path d="M6.6 10.8a15 15 0 0 0 6.6 6.6l2.2-2.2a1 1 0 0 1 1-.25 11.4 11.4 0 0 0 3.6.57 1 1 0 0 1 1 1V20a1 1 0 0 1-1 1A17 17 0 0 1 3 4a1 1 0 0 1 1-1h3.5a1 1 0 0 1 1 1c0 1.25.2 2.45.57 3.57a1 1 0 0 1-.25 1z"/></svg>
      </li>
      <li>314 555 0197
        <svg viewBox="0 0 24 24"><path d="M6.6 10.8a15 15 0 0 0 6.6 6.6l2.2-2.2a1 1 0 0 1 1-.25 11.4 11.4 0 0 0 3.6.57 1 1 0 0 1 1 1V20a1 1 0 0 1-1 1A17 17 0 0 1 3 4a1 1 0 0 1 1-1h3.5a1 1 0 0 1 1 1c0 1.25.2 2.45.57 3.57a1 1 0 0 1-.25 1z"/></svg>
      </li>
      <li>wadel@corvinsacks.com
        <svg viewBox="0 0 24 24"><path d="M2 5h20v14H2zM4 7v.5l8 5 8-5V7z"/></svg>
      </li>
    </ul>

    <p class="website">corvinsacks.com</p>
  </section>
</main>
</body>
</html>
```